Banner Design for Holistic Clinic

We need a banner to be designed for a Holistic Clinic which treats patient using IV Nutrition therapy, IV Vitamin C therapy, Chelation therapy, Homoepathy , Accupuncture, Ayurveda. Our website is www.verdantcarehub.in

We need the banner to show case all our services. IV Nutrition therapy, IV Vitamin C therapy, Chelation therapy, Homoepathy , Accupuncture, Ayurveda with special emphasis on IV Therapies. This will be in the front of the web page and will be used for leaflets and flex material.Ideally

I like the concept of IV infsuion bags, fruits etc. I have attached some of the pic which i liked. Please see the attachment "banner clinic july 13" But feel free to change it and bring in something better that will showcase all our services together

Target Market(s)

30 plus Adults

Industry/Entity Type

Health And Wellness

Font styles to use
Serif

Colors
acd036
f37122
33a6d7

Requirements
Must have
• Some samples are given below. It got to be colourful, yet pleasing.

```html
<!DOCTYPE html>
<html lang="en">
<head>
<meta charset="utf-8">
<title>Verdant Care Hub</title>
<link href="https://fonts.googleapis.com/css2?family=Josefin+Sans:wght@400;600;700&family=Roboto:wght@400;700&family=Share+Tech+Mono&display=swap" rel="stylesheet">
<style>
:root{
  --green:#acd036;
  --green-deep:#2e9a3a;
  --orange:#f37122;
  --blue:#33a6d7;
  --red:#d8232a;
  --ink:#222;
  --muted:#555;
  --cream:#f7f4e6;
}
*{margin:0;padding:0;box-sizing:border-box}
html,body{width:1200px;height:1200px;overflow:hidden;background:#fff}
body{position:relative;font-family:'Josefin Sans',sans-serif;color:var(--ink)}
.header{position:absolute;left:0;top:0;width:1200px;height:119px;background:#fff}
.brand{position:absolute;left:166px;top:14px;display:flex;align-items:center;gap:8px}
.brand-mark{width:40px;height:40px;background:var(--green-deep);border-radius:50%}
.brand-text small{display:block;font-family:'Share Tech Mono',monospace;font-size:8px;color:#444}
.brand-text strong{display:block;font-family:'Josefin Sans',sans-serif;font-weight:700;font-size:19px;color:var(--green-deep);letter-spacing:.5px;line-height:1.1}
.brand-text em{display:block;font-style:normal;font-size:7px;color:#666}
.phone{position:absolute;left:755px;top:22px;display:flex;align-items:center;gap:8px;font-size:19px;letter-spacing:.5px}
.phone-icon{width:33px;height:30px;background:var(--green);display:flex;align-items:center;justify-content:center}
.divider{position:absolute;left:170px;top:81px;width:860px;border-top:1px dashed #ccc}
.nav{position:absolute;left:0;top:94px;width:1200px;display:flex;justify-content:center;gap:30px;font-size:15px;letter-spacing:.5px}
.nav .active{color:var(--red)}
.hero{position:absolute;left:0;top:119px;width:1200px;height:411px;background:radial-gradient(ellipse at 30% 40%,#f4c842,#e8b62a 55%,#c99b24 100%)}
.hero-title{position:absolute;top:103px;width:1200px;text-align:center;font-family:'Roboto',sans-serif;font-size:36px;color:#fff;white-space:nowrap}
.hero-title b{font-weight:700}
.hero-title .bar{color:var(--green);margin:0 14px;font-weight:400}
.hero-title .light{font-weight:400}
.services{position:absolute;top:183px;left:0;width:1200px}
.service{position:absolute;width:148px;height:148px;border-radius:50%;background:var(--cream);border:4px solid var(--green);box-shadow:inset 0 0 0 1px #e8e2c4;display:flex;flex-direction:column;align-items:center;padding-top:14px}
.service svg{width:54px;height:64px}
.service span{font-family:'Roboto',sans-serif;font-size:17.5px;color:var(--blue);text-align:center;line-height:1.25;margin-top:2px}
.suffer{position:absolute;left:0;top:530px;width:1200px;height:350px;background:linear-gradient(135deg,#3aa33c,#2b8f2e 50%,#3aa33c)}
.suffer h2{position:absolute;top:26px;width:1200px;text-align:center;font-size:40px;font-weight:600;color:#fff}
.cond-col{position:absolute;top:88px;width:210px;list-style:none;color:#fff;font-size:13.5px;font-weight:600}
.cond-col li{position:relative;padding-left:11px;margin-bottom:11.5px;line-height:1.25}
.cond-col li::before{content:"";position:absolute;left:0;top:6px;width:3px;height:3px;border-radius:50%;background:#fff}
.treat-art{position:absolute;left:160px;top:950px;width:350px;height:250px;background:linear-gradient(160deg,#e4f2c8,#2fa9d9 60%,#1c87c0);border-radius:24px 24px 0 0}
.leaf-art{position:absolute;left:1035px;top:880px;width:160px;height:110px;background:radial-gradient(ellipse,#6ec834,#3d9c23 60%,rgba(255,255,255,0) 72%)}
.treat{position:absolute;left:535px;top:952px;width:500px}
.treat h2{font-size:35px;font-weight:400;line-height:1.12;color:var(--red)}
.treat h2 .g{color:var(--green-deep)}
.treat .rule{width:78px;border-top:2px solid #bbb;margin:6px 0 0}
.treat p{font-size:13.5px;color:var(--muted);line-height:1.45;margin-top:26px;width:490px}
.therapies{display:grid;grid-template-columns:211px 211px;margin-top:14px;list-style:none;font-size:13.5px;color:#333}
.therapies li{position:relative;padding-left:23px;height:27px}
.therapies li::before{content:"";position:absolute;left:4px;top:3px;width:5px;height:5px;border:1px solid #999;border-radius:50%}
</style>
</head>
<body>
<header class="header">
  <div class="brand">
    <div class="brand-mark"></div>
    <div class="brand-text">
      <small>Dr. Elena Varga's (MBBS, MD)</small>
      <strong>VERDANT CARE HUB</strong>
      <em>Allopathy, Ayurveda, Homeopathy, Acupuncture/Sujok</em>
    </div>
  </div>
  <div class="phone">
    <div class="phone-icon"><svg width="10" height="16" viewBox="0 0 10 16"><rect x="1" y="1" width="8" height="14" rx="1.5" fill="none" stroke="#fff" stroke-width="1.5"/><circle cx="5" cy="12.5" r="0.9" fill="#fff"/></svg></div>
    <span>9810 442 615, 8820 553 104</span>
  </div>
  <div class="divider"></div>
  <nav class="nav"><span class="active">Home</span><span>About us</span><span>Services ⌄</span><span>Work with us</span><span>Videos</span><span>Contact us</span></nav>
</header>

<section class="hero" role="img" aria-label="Photo of citrus slices, green leaves and amber dropper bottles on yellow">
  <h1 class="hero-title"><b>VERDANT CARE HUB</b><span class="bar">|</span><span class="light">OUR SERVICES</span></h1>
  <div class="services">
    <div class="service" style="left:93px"><svg viewBox="0 0 54 64"><path d="M27 2 C20 20 7 30 7 42 a20 20 0 0 0 40 0 C47 30 34 20 27 2Z" fill="var(--green)"/><circle cx="27" cy="44" r="11" fill="none" stroke="#fff" stroke-width="2.5"/></svg><span>IV Nutrition<br>Therapy</span></div>
    <div class="service" style="left:266px"><svg viewBox="0 0 54 64"><path d="M27 2 C20 20 7 30 7 42 a20 20 0 0 0 40 0 C47 30 34 20 27 2Z" fill="var(--orange)"/><path d="M30 52 a10 10 0 0 1 8 -14" fill="none" stroke="#fff" stroke-width="2.5"/></svg><span>IV Vitamin C<br>Therapy</span></div>
    <div class="service" style="left:439px"><svg viewBox="0 0 54 64"><path d="M27 2 C20 20 7 30 7 42 a20 20 0 0 0 40 0 C47 30 34 20 27 2Z" fill="var(--blue)"/><path d="M18 40 a10 10 0 0 0 10 12" fill="none" stroke="#fff" stroke-width="2.5"/></svg><span>Chelation<br>Therapy</span></div>
    <div class="service" style="left:613px"><svg viewBox="0 0 54 64"><path d="M10 58 C14 36 30 24 52 22 C48 44 32 54 14 52" fill="var(--green)"/><path d="M4 10 C16 10 24 18 24 30 C12 30 6 22 4 10Z" fill="#7fbf2a"/></svg><span>Homoepathy</span></div>
    <div class="service" style="left:786px"><svg viewBox="0 0 54 64"><circle cx="27" cy="32" r="20" fill="none" stroke="var(--orange)" stroke-width="3"/><circle cx="27" cy="32" r="4" fill="var(--orange)"/></svg><span>Accupuncture</span></div>
    <div class="service" style="left:959px"><svg viewBox="0 0 54 64"><circle cx="27" cy="32" r="22" fill="none" stroke="var(--blue)" stroke-width="3"/><circle cx="27" cy="32" r="7" fill="none" stroke="var(--blue)" stroke-width="3"/></svg><span>Ayurveda</span></div>
  </div>
</section>

<section class="suffer">
  <h2>Are you suffering from ?</h2>
  <ul class="cond-col" style="left:169px"><li>Cardio Vascular Diseaes</li><li>Menstrual Disorders</li><li>Stroke/Paralysis</li><li>Migraine</li><li>Acidity</li><li>Muscular and Joint Pain</li><li>Arthiritis</li><li>Obesity</li></ul>
  <ul class="cond-col" style="left:392px"><li>Astma</li><li>Parkinsonim</li><li>Back Ache</li><li>Prostrate Gland Enlasrgement</li><li>Body Pain</li><li>Psoriasis</li><li>Cervical and Lumbar Spondylosis</li></ul>
  <ul class="cond-col" style="left:615px;width:190px"><li>Sciatica</li><li>Cramps</li><li>Sinsuitis</li><li>Disc slips and disc prolaps</li><li>Snoring</li><li>Fibroid</li><li>Stress</li></ul>
  <ul class="cond-col" style="left:837px"><li>Hypertension</li><li>Tennis Elbow</li><li>Insomnia</li><li>Thyroid Issues</li><li>Kidney</li><li>Disorders</li><li>Ulcer</li></ul>
</section>

<div class="leaf-art" role="img" aria-label="Cluster of fresh green leaves"></div>
<div class="treat-art" role="img" aria-label="Illustration of a doctor in blue scrubs with stethoscope framed by leaf shapes"></div>

<section class="treat">
  <h2>We treat <span class="g">holistically</span> using a combination of</h2>
  <div class="rule"></div>
  <p>We are a “No SURGERY” centre dedicated to treating various diseases without Surgery. We treat holistically using a combination of</p>
  <ul class="therapies">
    <li>Allopathy</li><li>Arterio Clearance Therapy</li>
    <li>Homeopathy</li><li>Ayurveda</li>
    <li>IV Nutrition Therapy</li><li>Hijama Cupping Therapy</li>
    <li>Acupuncture / Sujok</li><li>Yoga</li>
  </ul>
</section>
</body>
</html>
```